Full redesign of dairy products including Yogurts and milk products

We have been selling milk and yogurts over the past 15 years, we are now expanding into a wider range of dairy products to include flavoured milk and a variety of soft cheeses such as cottage cheese etc. It is now the perfect time to redesign our existing product range to give a fresh and new look to our products. Have a look at our website https://rtvale.co.uk/ for further details. We are rebranding as NUVELKA, I have attached a identify pack to give you a feel of the the design, this is a fresh and bright design that will reflect the fresh and tasteful products we produce. The current milk label cut out is unique to us and I would like to continue using this shape which I have attached, the other labels should be done using regular rectangular rounded edge labels. The following designs are required;
1 x Universal lid (71.5mm) design for all below 120ml Yogurts
-11 x 120 ml Yogurt pot designs
Strawberry
Strawberry Banana
Peach & Apricot
Cherry
Toffee
Vanilla
Natural
Orange
Forest Fruits
Pineapple
Mango
1 x Universal lid (95.5mm)for below yogurts (can be identical to the 120ml Lid)
-4 x 450ml Yogurt Pots
Strawberry
Natural
Toffee
Mango
-1 x Universal (95.5mm) LID for 150ml Greek Yogurt
-4 x Designs for 150ml Greek yogurt POT
Strawberry
Natural
Vanilla
Mango

3 x Flavoured milk labels 2 sizes 250ml & 1lt
Biscotti
Chocolate
Strawberry

Cottage Cheese Lid & Pot 250g

1 x Quark universal Lid (95.5mm)
4 x Quark 250g pots
Natural
Strawberry
Peach & Apricot
Mango

```html
<!DOCTYPE html>
<html lang="en">
<head>
<meta charset="utf-8">
<title>NUVELKA Strawberry Milk Label</title>
<link rel="stylesheet" href="https://fonts.googleapis.com/css2?family=Poppins:wght@500;700;800&family=Playfair+Display:wght@900&family=Roboto+Slab:wght@700&display=swap">
<style>
  :root{
    --page:#dedede;
    --white:#ffffff;
    --blush:#f6d5d6;
    --rose:#e48a8f;
    --berry:#d6454b;
    --milk-red:#c7161f;
    --milk-dark:#8e0c12;
    --green:#2d8a1c;
    --green-dark:#226d14;
  }
  *{margin:0;padding:0;box-sizing:border-box}
  html,body{width:1200px;height:1199px;overflow:hidden;background:var(--page)}
  .canvas{position:relative;width:1200px;height:1199px;display:flex;align-items:center;justify-content:center}
  .label{
    position:relative;width:1040px;height:560px;
    background:linear-gradient(90deg,var(--blush) 0%,var(--white) 22%,var(--white) 48%,var(--white) 62%,var(--rose) 100%);
    border-bottom:7px solid var(--green);
    overflow:hidden;
  }
  .label::before{
    content:"";position:absolute;inset:0;
    background:linear-gradient(180deg,rgba(246,213,214,.7) 0%,rgba(255,255,255,0) 45%);
  }
  .brand{
    position:absolute;left:150px;top:34px;
    font-family:"Poppins",sans-serif;font-weight:800;font-size:64px;
    color:var(--green);letter-spacing:1px;
  }
  .flavour{position:absolute;left:110px;top:140px;width:360px;height:90px}
  .flavour text{font-family:"Roboto Slab",serif;font-weight:700;font-size:40px;fill:var(--white)}
  .product{
    position:absolute;left:96px;top:210px;
    font-family:"Playfair Display",serif;font-weight:900;font-size:170px;line-height:1;
    color:var(--milk-red);
    background:linear-gradient(180deg,var(--milk-red) 0%,var(--milk-dark) 100%);
    -webkit-background-clip:text;background-clip:text;-webkit-text-fill-color:transparent;
  }
  .claims{position:absolute;left:70px;top:410px;list-style:none;width:200px}
  .claims li{
    display:flex;align-items:center;gap:8px;
    font-family:"Poppins",sans-serif;font-weight:500;font-size:26px;color:var(--green);
    border-bottom:1.5px solid var(--green);padding:1px 0;
  }
  .claims svg{width:20px;height:20px;flex:none}
  .badge{position:absolute;left:330px;top:420px;width:120px;height:120px}
  .badge text{font-family:"Poppins",sans-serif;font-weight:700;fill:var(--white);text-anchor:middle}
  .fruit-art{
    position:absolute;left:480px;top:40px;width:500px;height:500px;border-radius:50%;
    background:radial-gradient(circle at 50% 55%,var(--milk-red) 0%,var(--berry) 30%,rgba(230,120,125,.55) 60%,rgba(255,255,255,0) 72%);
  }
  .volume{
    position:absolute;right:40px;bottom:20px;
    font-family:"Poppins",sans-serif;font-weight:700;font-size:26px;color:var(--green-dark);
  }
</style>
</head>
<body>
<main class="canvas">
  <section class="label">
    <div class="brand">NUVELKA</div>

    <svg class="flavour" viewBox="0 0 360 90" aria-hidden="false">
      <path d="M10 30 Q20 12 60 14 L330 22 Q350 24 352 44 Q352 66 330 68 L60 74 Q20 76 12 60 Z" fill="var(--green)"/>
      <text x="40" y="58">Strawberry</text>
    </svg>

    <div class="product">Milk</div>

    <ul class="claims">
      <li><svg viewBox="0 0 20 20"><path d="M10 2 C6 8 4 11 4 13 a6 6 0 0 0 12 0 C16 11 14 8 10 2Z" fill="none" stroke="var(--green)" stroke-width="1.6"/></svg>Fresh</li>
      <li><svg viewBox="0 0 20 20"><path d="M3 17 C3 8 9 3 17 3 C17 11 12 17 3 17Z M3 17 L12 8" fill="none" stroke="var(--green)" stroke-width="1.6"/></svg>Natural</li>
      <li><svg viewBox="0 0 20 20"><path d="M3 12 a7 5 0 0 0 14 0 Z M10 3 v5" fill="none" stroke="var(--green)" stroke-width="1.6"/></svg>Delicious</li>
    </ul>

    <svg class="badge" viewBox="0 0 120 120">
      <polygon fill="var(--green)" points="60,4 68,14 80,8 84,20 97,19 96,32 108,37 102,48 112,56 102,64 108,75 96,80 97,93 84,92 80,104 68,98 60,108 52,98 40,104 36,92 23,93 24,80 12,75 18,64 8,56 18,48 12,37 24,32 23,19 36,20 40,8 52,14"/>
      <text x="60" y="40" font-size="11">DIETIC</text>
      <text x="60" y="66" font-size="26">0.3%</text>
      <text x="60" y="80" font-size="10">MILK</text>
      <text x="60" y="92" font-size="10">FAT</text>
    </svg>

    <div class="fruit-art" role="img" aria-label="Photograph of a whole strawberry surrounded by halved strawberries"></div>

    <div class="volume">1L</div>
  </section>
</main>
</body>
</html>
```